Magazine Ad for the Waste Industry

We need a full page ad design that will help us introduce our new engine cooling system into the Waste market. This system helps regulate engine temperatures for large trash trucks with its advanced technology and durable. We would like this ad to make an impact and stand out from the more cluttered looking ads that are seen in trade magazines.
The project must be submitted in either InDesign or Photoshop files.

Target Market(s)

Waste Industry, Trash truck manufacturers

Industry/Entity Type

Waste Management

Font styles to use
Sans Serif

Colors
0255a3

Requirements
Must have
• The text and images attached with a more modern industrial/masculine feel.
• Our Company colors are...
• Blue (RGB 25, 76, 159)
• Gray (RGB 129, 130, 133)
• White and black as accents as needed
• SIZING
• Spread Bleed: 9.5" x 11.375"
Nice to have
• I attached two files for a font that we have used in the past. Another font we use commonly is Ariel.

```html
<!DOCTYPE html>
<html lang="en">
<head>
<meta charset="utf-8">
<title>Advanced Electric Engine Cooling — Vantra</title>
<link href="https://fonts.googleapis.com/css2?family=Michroma&display=swap" rel="stylesheet">
<style>
  :root {
    --ink: #020509;
    --deep-blue: #062a55;
    --brand-blue: #194c9f;
    --steel: #818285;
    --gold: #e6c65a;
    --white: #ffffff;
  }
  html, body {
    margin: 0;
    padding: 0;
    width: 849px;
    height: 1200px;
    overflow: hidden;
    background: var(--ink);
  }
  .ad {
    position: relative;
    width: 849px;
    height: 1200px;
    overflow: hidden;
    background:
      radial-gradient(ellipse 520px 460px at 330px 230px, rgba(150,205,240,0.85), rgba(40,120,190,0.55) 45%, rgba(6,42,85,0) 80%),
      linear-gradient(180deg, #1f6fae 0%, #0c4a86 30%, var(--deep-blue) 52%, #020d1c 68%, var(--ink) 82%);
  }
  .hero-product {
    position: absolute;
    left: 232px;
    top: 120px;
    width: 440px;
    height: 510px;
    background: radial-gradient(ellipse at 50% 45%, rgba(210,230,245,0.55), rgba(30,40,55,0.9) 55%, rgba(10,20,35,0) 75%);
    border-radius: 40%;
  }
  .swoosh {
    position: absolute;
    left: 0;
    top: 0;
    width: 849px;
    height: 1200px;
  }
  .headline {
    position: absolute;
    left: 0;
    top: 700px;
    width: 849px;
    height: 240px;
  }
  .headline text {
    font-family: "Michroma", sans-serif;
    stroke-width: 2.6;
    stroke-linejoin: round;
  }
  .benefits {
    position: absolute;
    left: 0;
    top: 964px;
    width: 849px;
    margin: 0;
    text-align: center;
    font-family: "Michroma", sans-serif;
    font-style: italic;
    font-size: 14px;
    line-height: 22.4px;
    color: var(--white);
  }
  .benefits .gold { color: var(--gold); }
  .benefits .sep {
    display: inline-block;
    width: 5px;
    height: 5px;
    border: 2px solid var(--gold);
    border-radius: 2px;
    margin: 0 6px 2px;
    vertical-align: middle;
  }
  .brand-name {
    position: absolute;
    left: 68px;
    top: 1108px;
    font-family: "Michroma", sans-serif;
    font-size: 22px;
    line-height: 30px;
    color: var(--brand-blue);
  }
  .partner-badge {
    position: absolute;
    left: 220px;
    top: 1104px;
    width: 58px;
    height: 46px;
    background: var(--white);
  }
  .web-address {
    position: absolute;
    left: 538px;
    top: 1137px;
    font-family: "Michroma", sans-serif;
    font-size: 11.5px;
    color: var(--white);
    letter-spacing: 0.6px;
  }
</style>
</head>
<body>
<main class="ad">
  <div class="hero-product" role="img" aria-label="Electric engine cooling unit with four reversible fans bursting through icy water splash"></div>

  <svg class="swoosh" viewBox="0 0 849 1200" aria-hidden="true">
    <defs>
      <linearGradient id="swooshGold" x1="0" y1="0" x2="1" y2="0">
        <stop offset="0" stop-color="#e6c65a" stop-opacity="0"/>
        <stop offset="0.45" stop-color="#f2dc8a"/>
        <stop offset="1" stop-color="#e6c65a"/>
      </linearGradient>
    </defs>
    <path d="M420 658 C 580 652 740 600 849 480 L 849 520 C 760 610 600 660 420 658 Z" fill="url(#swooshGold)"/>
    <path d="M420 660 C 600 664 760 620 849 524 L 849 534 C 760 628 600 668 420 660 Z" fill="#ffffff" opacity="0.55"/>
  </svg>

  <svg class="headline" viewBox="0 700 849 240" aria-label="Advanced Electric Engine Cooling">
    <defs>
      <linearGradient id="chrome" x1="0" y1="0" x2="0" y2="1">
        <stop offset="0" stop-color="#f4f5f6"/>
        <stop offset="0.5" stop-color="#b9bbbe"/>
        <stop offset="1" stop-color="#818285"/>
      </linearGradient>
      <linearGradient id="iceText" x1="0" y1="0" x2="1" y2="0">
        <stop offset="0" stop-color="#1b8fc6"/>
        <stop offset="0.5" stop-color="#9fdcf5"/>
        <stop offset="1" stop-color="#1b8fc6"/>
      </linearGradient>
    </defs>
    <text x="110" y="772" font-size="78" fill="url(#chrome)" stroke="url(#chrome)" textLength="646" lengthAdjust="spacingAndGlyphs">ADVANCED</text>
    <text x="110" y="866" font-size="98" fill="url(#chrome)" stroke="url(#chrome)" textLength="646" lengthAdjust="spacingAndGlyphs">ELECTRIC</text>
    <text x="110" y="926" font-size="54" fill="url(#iceText)" stroke="url(#iceText)" textLength="646" lengthAdjust="spacingAndGlyphs">ENGINE COOLING</text>
  </svg>

  <p class="benefits">
    <span class="gold">FULLY REVERSIBLE FANS</span><span class="sep"></span>ELIMINATE<br>
    PREVENTATIVE MAINTENANCE<span class="sep"></span><span class="gold">QUIETER</span><br>
    <span class="gold">RESIDENTIAL OPERATION</span><span class="sep"></span>AVERAGE 8% FUEL<br>
    ECONOMY<span class="sep"></span><span class="gold">INCREASE HORSEPOWER</span>
  </p>

  <div class="brand-name">VANTRA</div>
  <div class="partner-badge" role="img" aria-label="Partner program badge"></div>

  <div class="web-address">www.vantra-corp.com/refuse</div>
</main>
</body>
</html>
```